Monthly Newsletter template required for the Irish in London. Read on...

During Summer 2014, a new web site for the Irish in London will launch - www.bantrovo.com. The purpose of the site is to list all Irish-related activities happening in London inc gigs, sport, arts and culture, business and networks, community, meetups etc.

Each month the database will be sent a monthly e newsletter.
We have linked up with an individual who has been producing a monthly newsletter for some time. The format of his letter is a standard email featuring loads of links and copy. Content rich but with no order or visuals. (copy attached). His newsletter is called 'Moss Whispers Weekly' and we're going to stick with the name because it gets people's attention. However, it will be a Bantrovo product.

We want the newsletter template to feature an iconic image of Moss, who is the writer of the newsletter. Think of him as a incognito, a spy or a mole. He's mysterious...So, the Moss Whispers image for the template needs to reflect this.

The newsletter template design can't be too corporate or too casual as the audience is broad spectrum. It has to be original.

Please note - no shamrocks, leprechauns required though the use of the colour green, in some way, would be good.

Thanks for reading :D

Target Market(s)

The audience main age range is:
Irish
Based in London
Ages: 22 to 45
Crossing over a broad spectrum of occuptations

Industry/Entity Type

Business

Requirements
Must have
• Good content order so that each reader can access their interest areas quickly and easily.
Categories:

Gigs
Sport
Business & Networks
Arts & Culture
Education & General Interest
Community
Charities
Other
Nice to have
• Create a Mooss Whispers image that suggests he's mysterious detective. Maybe a silouette of a man in a trench coat and fedora hat? We want the newletter to have a personality.

I've included an image of such a character below. Like the siihouette only and the 'Grey Quiet Rogue' which could be changed to 'Moss Whispers'
Should not have
• Shamrocks or leprechauns

Look and feel must not look too corporate or too casual.

```html
<!DOCTYPE html>
<html lang="en">
<head>
<meta charset="utf-8">
<title>Bantrovo – Moss Whispers Weekly</title>
<link rel="stylesheet" href="https://fonts.googleapis.com/css2?family=Open+Sans:wght@400;600;700&display=swap">
<style>
:root{
  --green:#1fc98e;
  --red:#e0484a;
  --ink:#222;
  --text:#333;
  --rule:#d9d9d9;
  --sand:#efefe2;
  --mist:#ececf1;
  --grey:#ebebeb;
  --night:#1b2344;
  --footer:#2e2e2e;
  --white:#fff;
}
*{box-sizing:border-box;margin:0;padding:0}
html,body{width:1200px;height:4182px;overflow:hidden;background:var(--white)}
body{font-family:"Open Sans",Arial,sans-serif;color:var(--text)}
.newsletter{position:relative;width:1200px;height:4182px}
section,header,footer{position:relative;width:1200px;overflow:hidden}
.abs{position:absolute}
.section-title{position:absolute;left:26px;font-size:44px;font-weight:400;color:var(--ink);letter-spacing:-.3px}
.body-copy{font-size:25px;line-height:40px;color:var(--text)}

/* brand name (plain wordmark stand-in) */
.brand{display:flex;align-items:center;gap:22px}
.brand-dot{width:54px;height:54px;border-radius:50%;background:var(--green);flex:none}
.brand-name{font-size:72px;font-weight:700;line-height:80px;color:var(--green)}

/* header */
.masthead{height:402px;background:linear-gradient(180deg,#2a335a 0%,var(--night) 55%,#141a33 100%)}
.masthead .skyline{left:0;top:0;width:1200px;height:402px;background:radial-gradient(ellipse 420px 260px at 640px 160px,rgba(140,150,190,.35),rgba(0,0,0,0) 70%)}
.url-pill{left:820px;top:19px;width:338px;height:39px;border-radius:20px;background:rgba(255,255,255,.85);color:#333;font-size:22px;line-height:39px;text-align:center}
.masthead .brand{position:absolute;left:260px;top:280px}

/* business */
.business{height:357px;border-bottom:2px solid var(--rule)}
.business .section-title{top:30px}
.business .rule{left:26px;top:106px;width:1148px;height:2px;background:var(--rule)}
.business .body-copy{left:26px;top:122px;width:1150px}
.btn-green{left:939px;top:278px;width:200px;height:62px;border-radius:31px;background:var(--green);color:var(--white);font-size:23px;font-weight:600;line-height:62px;text-align:center}

/* sports headlines */
.sports-headlines{height:447px;background:var(--sand)}
.sports-headlines .photo{left:16px;top:36px;width:554px;height:386px;background:linear-gradient(135deg,#0f7a45,#1ea862 50%,#0c5e35)}
.sports-headlines .section-title{left:611px;top:40px}
.sports-headlines .rule{left:611px;top:106px;width:563px;height:2px;background:var(--rule)}
.headline-list{left:611px;top:150px;width:560px;list-style:none}
.headline-list li{position:relative;padding-left:40px;font-size:25px;line-height:35px;margin-bottom:16px}
.chev{position:absolute;left:0;top:8px;width:18px;height:20px}
.band{height:16px;background:var(--green)}

/* arts */
.arts{height:747px;background:var(--mist)}
.arts .section-title{top:18px}
.arts .section-title b{font-weight:700}
.card{top:74px;width:553px;height:643px;background:var(--white)}
.card .photo{left:0;top:0;width:553px;height:294px}
.card h3{position:absolute;left:30px;top:318px;width:500px;font-size:38px;line-height:46px;font-weight:400;color:var(--ink)}
.card .divider{left:0;top:425px;width:553px;height:2px;background:var(--rule)}
.card .body-copy{left:30px;top:445px;width:500px;font-size:24px;line-height:38px}
.card .foot{left:0;top:585px;width:553px;height:58px;background:var(--green)}
.card .foot svg{position:absolute;right:22px;top:14px}

/* sports grid */
.sports-grid{height:781px}
.sports-grid .section-title{top:52px}
.tile{top:109px;width:354px;height:640px}
.tile .photo{left:0;top:0;width:354px;height:225px}
.tile h3{position:absolute;left:0;top:240px;font-size:36px;font-weight:600;color:var(--ink)}
.tile .body-copy{left:0;top:295px;width:354px;font-size:24px;line-height:37px}
.btn-outline{left:36px;top:578px;width:200px;height:64px;border:2px solid var(--rule);border-radius:32px;font-size:23px;line-height:60px;text-align:center;color:#333;background:var(--white)}

/* education */
.education{height:387px;background:var(--grey)}
.education .section-title{top:40px}
.education .body-copy{left:26px;top:130px;width:590px;font-size:24px;line-height:37px}
.education .photo{left:627px;top:48px;width:554px;height:290px;background:linear-gradient(135deg,#c9c2b8,#e7e3dc 45%,#8d8a86)}

/* community, gigs, charity */
.columns{height:530px}
.col-title{position:absolute;font-size:44px;font-weight:600;color:var(--ink)}
.community-list{left:26px;top:140px;width:540px;list-style:none}
.community-list li{position:relative;padding-left:40px;font-size:24px;line-height:38px;margin-bottom:36px}
.gigs-copy,.charity-copy{left:624px;width:550px;font-size:24px;line-height:38px;border-top:2px solid var(--rule);padding-top:14px}
.gigs-copy{top:120px}
.charity-copy{top:360px}

/* footer */
.footer{height:515px;background:var(--footer);color:#ddd}
.footer .managed{right:26px;top:40px;text-align:right;font-size:25px;line-height:38px}
.enquiry-pill{right:26px;top:145px;width:350px;height:42px;border-radius:21px;background:#d8d8d8;color:#333;font-size:22px;line-height:42px;text-align:center}
.footer .brand{position:absolute;left:40px;top:400px}
.social{right:26px;top:415px;display:flex;gap:20px}
.social span{display:block;width:64px;height:64px;border-radius:50%;border:3px solid #ddd}
</style>
</head>
<body>
<div class="newsletter">

  <header class="masthead">
    <div class="abs skyline" role="img" aria-label="Night-time London skyline with a cathedral dome"></div>
    <div class="abs url-pill">http://www.bantrovo.com</div>
    <div class="brand"><span class="brand-dot"></span><span class="brand-name">Bantrovo</span></div>
  </header>

  <section class="business">
    <h2 class="section-title">Business &amp; Networks</h2>
    <div class="abs rule"></div>
    <p class="abs body-copy">Economic Business Overview on Thursday the 12th at NBF, Harlow House, 4 Tanner Row, EC3V 9QT. Declan Hart (Chief Economist, NBF) will outline a snapshot of the economy, an accurate and timely assessment of the macroeconomic scene and a guide to future trends in the economy in the rapidly changing economic situation</p>
    <div class="abs btn-green">READ MORE</div>
  </section>

  <section class="sports-headlines">
    <div class="abs photo" role="img" aria-label="Green Ireland supporters' jerseys"></div>
    <h2 class="section-title">Sports</h2>
    <div class="abs rule"></div>
    <ul class="abs headline-list">
      <li><svg class="chev" viewBox="0 0 18 20"><path d="M3 2l10 8-10 8" fill="none" stroke="#e0484a" stroke-width="3"/></svg>Ireland opt for experience for second Test against Argentina</li>
      <li><svg class="chev" viewBox="0 0 18 20"><path d="M3 2l10 8-10 8" fill="none" stroke="#e0484a" stroke-width="3"/></svg>Ireland and Ulster mourn 1948 Grand Slam hero Tommy Rourke</li>
      <li><svg class="chev" viewBox="0 0 18 20"><path d="M3 2l10 8-10 8" fill="none" stroke="#e0484a" stroke-width="3"/></svg>Ireland and Ulster mourn 1948 Grand Slam hero Tommy Rourke</li>
    </ul>
  </section>

  <div class="band"></div>

  <section class="arts">
    <h2 class="section-title">Arts &amp; <b>Culture</b></h2>
    <article class="abs card" style="left:26px">
      <div class="abs photo" role="img" aria-label="Wooden Irish flute" style="background:linear-gradient(180deg,#9a9a9a,#cfcfcf 55%,#8a5a3a)"></div>
      <h3>Traditional Irish Musical Instruments</h3>
      <div class="abs divider"></div>
      <p class="abs body-copy">Irish Traditional Music for Beginners, Improvers and Advanced Musicians. Classes Available</p>
      <div class="abs foot"><svg width="30" height="30" viewBox="0 0 30 30" fill="none" stroke="#fff" stroke-width="3"><path d="M12 5H5v20h20v-7M17 5h8v8M25 5L13 17"/></svg></div>
    </article>
    <article class="abs card" style="left:608px">
      <div class="abs photo" role="img" aria-label="Irish dancers' feet in white socks and black shoes" style="background:linear-gradient(180deg,#4a4a4a,#d8d8d8 50%,#2a2a2a)"></div>
      <h3>Traditional Irish Dancing for Adults</h3>
      <div class="abs divider"></div>
      <p class="abs body-copy">The Nora Quill Academy of Dance provides dance classes for adults and children in Hammersmith.</p>
      <div class="abs foot"><svg width="30" height="30" viewBox="0 0 30 30" fill="none" stroke="#fff" stroke-width="3"><path d="M12 5H5v20h20v-7M17 5h8v8M25 5L13 17"/></svg></div>
    </article>
  </section>

  <section class="sports-grid">
    <h2 class="section-title">Sports</h2>
    <article class="abs tile" style="left:16px">
      <div class="abs photo" role="img" aria-label="Green football jersey close-up" style="background:linear-gradient(135deg,#0b6b3d,#20a863 55%,#0a5432)"></div>
      <h3>Irish Soccer</h3>
      <p class="abs body-copy">Construction &amp; Property Charity's football challenge 2014 on Sunday the 8th at the Pitchside Soccer Centre, Elmwood Way, New Malden, KT3 9ZX</p>
      <div class="abs btn-outline">READ MORE</div>
    </article>
    <article class="abs tile" style="left:399px">
      <div class="abs photo" role="img" aria-label="Green rugby balls" style="background:linear-gradient(135deg,#1c7a46,#6fbf7a 50%,#0d4d2c)"></div>
      <h3>Irish Rugby</h3>
      <p class="abs body-copy">The London Branch of the Shannonside Rugby Supporters Club will hold its AGM on Saturday the 14th at 5.30pm in their Central London base; Fenlows</p>
      <div class="abs btn-outline">READ MORE</div>
    </article>
    <article class="abs tile" style="left:782px">
      <div class="abs photo" role="img" aria-label="Hurling players with hurleys on grass" style="background:linear-gradient(180deg,#8fb36a,#5f8f3e 60%,#3d6b2a)"></div>
      <h3>Hurling</h3>
      <p class="abs body-copy">Western Gaels 2-12Played in Corrib Park last Sunday this was very much a game of two halves with the wind influencing proceedings throughout</p>
      <div class="abs btn-outline">READ MORE</div>
    </article>
  </section>

  <section class="education">
    <h2 class="section-title">Education &amp; General Interest</h2>
    <p class="abs body-copy">The Alder Centre has launched a new support project specifically for young Irish people. 'Una Farrell, our Mental Health Support and Liaison Officer, can help with lots of practical issues including finding employment, enrolling in education, claiming benefits and managing debt.</p>
    <div class="abs photo" role="img" aria-label="Classroom with students raising hands"></div>
  </section>

  <section class="columns">
    <h2 class="col-title" style="left:26px;top:40px">Community</h2>
    <ul class="abs community-list">
      <li><svg class="chev" viewBox="0 0 18 20"><path d="M3 2l10 8-10 8" fill="none" stroke="#e0484a" stroke-width="3"/></svg>The Irish and the British are deeply connected peoples. The UK is home to the largest Irish-born community outside of Ireland and to a vast number of people of Irish descent.</li>
      <li><svg class="chev" viewBox="0 0 18 20"><path d="M3 2l10 8-10 8" fill="none" stroke="#e0484a" stroke-width="3"/></svg>British citizens in Ireland outnumber all other non-Irish nationalities and topped the table for migrant workers registering for PPS numbers in 2013</li>
    </ul>
    <h2 class="col-title" style="left:624px;top:40px">Gigs</h2>
    <p class="abs gigs-copy">I couldn't let my event "Gigs Eire Presents a Music Industry Night" close without a review of a band that simply blew the venue away.</p>
    <h2 class="col-title" style="left:624px;top:280px">Charity</h2>
    <p class="abs charity-copy">Charities are part of all our lives. They range from small groups meeting local needs with few resources to the well-known major charities with budgets of millions.</p>
  </section>

  <footer class="footer">
    <div class="abs managed">Managed by Emerald Arts Collective Ltd<br>2nd Floor, Marlow Street, London, W1X 9QQ</div>
    <div class="abs enquiry-pill">enquiries: contact@bantrovo.com</div>
    <div class="brand"><span class="brand-dot"></span><span class="brand-name">Bantrovo</span></div>
    <div class="abs social" aria-label="Social links"><span></span><span></span><span></span><span></span><span></span></div>
  </footer>

</div>
</body>
</html>
```